Website for IT technology distribution company

Small business distributor of remote IT/Telecoms technology services in Canada

Looking for a bold, clean and professional design for WordPress. We would like a web site design from a designer who may be able to help us upload the site to WordPress (Ideally CSS files).
The website will have the following pages:
1) Home
2) Register
3) Packages
4) Contact

I am also attaching the company logo (with sourcefile, images for page 1 and details on wording/content for website)

Design must use colors that compliment the logo

Must Have:
- Must contain the logo in the header

Should Not Have:
- must not be blog or magazine style layout or look and feel

Industry/Entity Type

Business

```html
<!DOCTYPE html>
<html lang="en">
<head>
<meta charset="utf-8">
<title>Norvex Solutions Ltd — Register</title>
<link rel="stylesheet" href="https://fonts.googleapis.com/css2?family=Montserrat:wght@400;500;700&family=Open+Sans:wght@400;600&family=Oswald:wght@600;700&display=swap">
<style>
:root{
  --red:#e32b2b;
  --red-deep:#c41a22;
  --slate:#6a7891;
  --heading:#6b7589;
  --page:#f1f1f1;
  --footer:#444645;
  --footer-bar:#5e5f5e;
  --field:#6d7a93;
  --button:#333c4c;
  --white:#ffffff;
}
*{box-sizing:border-box;margin:0;padding:0}
html,body{width:1145px;height:1200px;overflow:hidden}
body{background:var(--page);font-family:'Open Sans',sans-serif;position:relative}
.site-header{position:absolute;top:0;left:0;width:1145px;height:95px;background:linear-gradient(#e4e6ea,#f4f4f6)}
.brand{position:absolute;left:156px;top:16px;font-family:'Montserrat',sans-serif;font-weight:700;color:var(--slate);font-size:34px;letter-spacing:-1px;line-height:1}
.brand small{display:block;font-size:13px;letter-spacing:0;margin-top:6px}
.social{position:absolute;top:8px;left:861px;display:flex;gap:9px}
.social span{width:32px;height:32px;border-radius:50%;background:var(--slate);border:2px solid #c9ced8;display:block}
.contact-line{position:absolute;top:69px;right:169px;display:flex;gap:14px;align-items:center;font-family:'Montserrat',sans-serif}
.contact-line .phone{font-weight:700;color:var(--slate);font-size:15px;display:flex;align-items:center;gap:5px}
.contact-line .mail{color:var(--slate);font-size:13px;display:flex;align-items:center;gap:5px}
.main-nav{position:absolute;top:95px;left:0;width:1145px;height:30px;background:var(--slate);border-top:1px solid #8a96ab}
.main-nav ul{list-style:none;position:absolute;right:172px;top:0;display:flex;height:30px}
.main-nav li{font-family:'Montserrat',sans-serif;color:var(--white);font-size:15px;line-height:30px;padding:0 22px;border-left:1px solid #8f9bb0}
.main-nav li:first-child{border-left:none}
.hero{position:absolute;top:125px;left:0;width:1145px;height:343px;background:linear-gradient(90deg,var(--red-deep),#e0434a 8%,var(--red-deep) 13%,transparent 13%,transparent 87%,var(--red-deep) 87%,#e0434a 92%,var(--red-deep))}
.hero-image{position:absolute;left:150px;top:0;width:845px;height:343px;background:linear-gradient(160deg,#d94450 0%,#eea3aa 35%,#f5dde0 65%,#eab4b9 100%)}
.hero-title{position:absolute;left:180px;top:180px;width:590px;font-family:'Oswald',sans-serif;font-weight:700;color:var(--white);font-size:23px;line-height:34px;letter-spacing:.4px;text-transform:uppercase;text-shadow:1px 1px 3px rgba(120,0,0,.7)}
.hero-fade{position:absolute;top:468px;left:0;width:1145px;height:40px;background:linear-gradient(#f4dcdd,var(--page))}
.section-title{position:absolute;left:165px;top:492px;font-family:'Montserrat',sans-serif;font-weight:700;color:var(--heading);font-size:32px;letter-spacing:1px}
.card{position:absolute;width:335px;height:199px;border-top:6px solid var(--red);box-shadow:6px 6px 10px rgba(0,0,0,.15);overflow:hidden}
.card .photo{position:absolute;inset:0}
.card p{position:absolute;color:var(--white);font-weight:600;font-size:19px;line-height:28px;text-shadow:1px 1px 3px rgba(0,0,0,.8)}
.card-phone{left:207px;top:540px}
.card-phone .photo{background:linear-gradient(120deg,#2a2d31,#4b5459 45%,#8a9397 75%,#dfe3e4)}
.card-phone p{left:10px;top:96px;width:320px}
.card-server{left:602px;top:540px}
.card-server .photo{background:linear-gradient(160deg,#3a3320,#1a1a18 40%,#0d0d0c)}
.card-server p{left:14px;top:74px;width:320px;font-size:18.5px;line-height:27px}
.card-keyboard{left:207px;top:774px}
.card-keyboard .photo{background:linear-gradient(170deg,#dde3ec,#3a4670 25%,#141a38 60%,#0b0f22)}
.card-keyboard p{left:16px;top:84px;width:315px}
.card-cta{left:602px;top:774px;background:var(--slate)}
.card-cta .cta-text{position:absolute;left:10px;top:46px;font-family:'Oswald',sans-serif;font-weight:700;font-size:50px;line-height:50px;color:#c3c6cc;letter-spacing:1px;text-transform:uppercase;text-shadow:2px 2px 3px rgba(0,0,0,.35)}
.card-cta .cta-art{position:absolute;left:240px;top:40px;width:85px;height:120px;background:radial-gradient(ellipse at center,rgba(230,232,236,.45),rgba(230,232,236,0) 70%)}
.site-footer{position:absolute;top:1000px;left:0;width:1145px;height:169px;background:var(--footer)}
.footer-heading{position:absolute;top:26px;font-family:'Montserrat',sans-serif;font-weight:700;color:var(--red);font-size:16px;letter-spacing:.5px}
.sitemap{position:absolute;left:167px;top:54px;list-style:none}
.sitemap li{font-family:'Montserrat',sans-serif;color:var(--white);font-size:13px;line-height:24px}
.field{position:absolute;width:208px;height:30px;background:var(--field);border:1px solid #8793a9;color:#e4e7ee;font-size:11.5px;padding:7px 11px}
.field.message{left:768px;top:51px;height:66px}
.send{position:absolute;left:768px;top:122px;width:208px;height:29px;background:var(--button);color:var(--white);font-family:'Montserrat',sans-serif;font-size:15px;text-align:center;line-height:29px;border:1px solid #56607a}
.copyright{position:absolute;top:1169px;left:0;width:1145px;height:31px;background:var(--footer-bar);color:#d6d6d6;font-size:11.5px;text-align:center;line-height:31px}
</style>
</head>
<body>
<header class="site-header">
  <div class="brand">NORVEX<small>Solutions Ltd</small></div>
  <div class="social" aria-label="Social links"><span></span><span></span><span></span></div>
  <div class="contact-line">
    <span class="phone"><svg width="13" height="12" viewBox="0 0 13 12"><path d="M1 4c0-2 3-3 5.5-3S12 2 12 4l-2 1-1-2H4L3 5z" fill="#e32b2b"/><rect x="3" y="6" width="7" height="5" rx="1" fill="#e32b2b"/></svg>1-416-555-0148</span>
    <span class="mail"><svg width="15" height="12" viewBox="0 0 15 12"><rect x="1" y="2" width="13" height="9" fill="none" stroke="#e32b2b" stroke-width="2"/><path d="M1 2l6.5 5L14 2" fill="none" stroke="#e32b2b" stroke-width="2"/></svg>info@norvex.ca</span>
  </div>
</header>
<nav class="main-nav"><ul><li>HOME</li><li>REGISTER</li><li>PACKAGES</li><li>CONTACT</li></ul></nav>
<section class="hero">
  <div class="hero-image" role="img" aria-label="Red globe linked by cables to laptops around it, on a red digital background"></div>
  <h1 class="hero-title">Imagine immediate access to highly trained Kestrel engineers, without the cost and expense of paying them for a site visit.</h1>
</section>
<div class="hero-fade"></div>
<h2 class="section-title">REGISTER</h2>
<article class="card card-phone"><div class="photo" role="img" aria-label="Office desk telephone close-up"></div><p>“Save up to 90% over traditional, on-site, engineering methods”</p></article>
<article class="card card-server"><div class="photo" role="img" aria-label="Row of server drive bays"></div><p>“Why pay a KESTREL engineer to sit and wait for work when you can have one when you need one and pay for only what you use”</p></article>
<article class="card card-keyboard"><div class="photo" role="img" aria-label="Keyboard close-up in blue light"></div><p>“Why put off until tomorrow what you can do today? Pay by the hour and have it done today”</p></article>
<article class="card card-cta"><div class="cta-text">Click for<br>Register</div>
  <div class="cta-art" role="img" aria-label="Computer mouse with signal waves"></div>
</article>
<footer class="site-footer">
  <h3 class="footer-heading" style="left:167px">SITE MAP</h3>
  <ul class="sitemap"><li>Home</li><li>Register</li><li>Packages</li><li>Contact</li></ul>
  <h3 class="footer-heading" style="left:547px">QUICK CONTACT</h3>
  <div class="field" style="left:550px;top:51px">Enter your name</div>
  <div class="field" style="left:550px;top:87px">Enter your email</div>
  <div class="field" style="left:550px;top:122px">Enter Subject</div>
  <div class="field message">Enter your message</div>
  <div class="send">Contact</div>
</footer>
<div class="copyright">Copyright © 2014 NORVEX &nbsp;| &nbsp;All rights reserved</div>
</body>
</html>
```